Web design for new streaming audio service

We need a homepage design for a new streaming audio service. Our company is called Olvantra, and we’re basically Vidorama for Audiobooks, Stand-Up Comedy, Lectures, Language Learning, etc. Essentially like Tunelark for everything audio EXCEPT music.
You don’t have to code the homepage (Design Only), but it should include 3 different designs to work with 1) Web; 2) Phones; 3) Tablets.
Below is a link to a mockup of the web version which gives a good idea of what elements we want. This is just a mockup and we want you to improve it.
Once you download the mockup, please refer to the more detailed instructions below:
The following outlines the design project for the Olvantra homepage. We have provided a rough mockup of the homepage layout that gives you a general idea of what we’re going for. There are a few elements that we are attached to, and many others where you have complete creative freedom to do whatever you think looks good.
The ZIP file includes the following:
* Mockup to see what we have in mind (olvantra-homepage-mockup.jpg)
* Text used (olvantra-homepage-text.txt)
* Raw image of actor (olvantra-actor1.jpg)
* Raw images for samples (olvantra-sample-[name].jpg)
Although we have only provided a mockup layout for the web version, we also need you to provide a mobile phone and a tablet version of the design also. It’s very possible the tablet version may be substantially similar to the web version, but the mobile phone version will likely be much different.
All of the raw files are included in the attached ZIP file. Please use our photographs and text as provided although cropping, sizing, etc. is flexible per the instructions below.
Display Requirements:
* Web Version - Minimum resolution 1024x768 (72 dpi) but should look good on 1920x1080 (72 dpi) - Page should be designed to scale to look acceptable in all resolutions in between.
* Phone Version - Minimum Zentro 4 - 640x960 (326 dpi) but should look good on Korvel Nimbus Q5 - 1920x1080 (441 dpi) - Page should be designed to scale to look acceptable in all resolutions and devices in between.
* Tablet Version - Minimum Pagewick Ember LX 7” - 1280x800 (216 dpi) but should also look good on a Slato Breeze - 2048x1536 (264 dpi) - Page should be designed to scale to look acceptable in all resolutions and devices in between.
Above the Fold - We want to make sure the Olvantra logo, Member Login Link, Large Photo, Headline, Price, Button, and the first row of sample images are all “Above the fold”. As a general guideline, this means 600 pixels high on a 1024x768 72 dpi web screen. This requirement is less important on Phone versions.
Top Logo Bar - We want to retain the blue bar with the Olvantra logo on the page, although we are open to a different size, shape and positioning if it greatly enhances the design. Please use the standard logo color, although you are welcome to use either the horizontal or vertical orientation of the logo based on your design.
Text color, font and size - Feel free to design the text in anyway you choose as long as the text is readable on the target platforms.
Buttons - Feel free to use any size, shape and colors for the buttons as long as they are obvious and clickable relative to the page. The only exception is the Chatterly button should follow the Chatterly color scheme and logo treatment (the mockup doesn’t seem 100% correct.)
Top Photograph - We want to retain the large photograph across the top of the screen although final shape and dimensions are flexible.
Size and shape of content samples (i.e. Audiobooks, Stand-Up Comedy, etc.) - Feel free to design the content samples in anyway you choose.
Three Sales Points (i.e. Listen on your Zentro…, All you can enjoy…, etc.) - The Three Sales Points are envisioned to each have a corresponding illustration which you should provide and have rights for. The placeholder is represented by a square next to the text. The color size and shape of these elements are flexible and can be designed in any way you choose.
Opt-in form - Feel free to design the opt-in form in anyway you choose as long as the text is readable and the interactivity is obvious on the target platforms.
Text links and copyright notice - Feel free to design the bottom of the page text links and copyright notice in anyway you choose.
Additional colors, graphic design elements, etc. - Feel free to use any additional colors, graphic design elements, etc. to support your design.

```html
<!DOCTYPE html>
<html lang="en">
<head>
<meta charset="utf-8">
<title>Olvantra — Stream Everything Audio</title>
<link href="https://fonts.googleapis.com/css2?family=Open+Sans:wght@300;400;600;700&display=swap" rel="stylesheet">
<style>
  :root{
    --sky:#5aa9d6;
    --sky-deep:#3f93c9;
    --sky-band-top:#6cb8df;
    --sky-band-bottom:#3a8ec6;
    --login:#1f6fb8;
    --orange:#f6921e;
    --orange-deep:#ec7a08;
    --link-blue:#2d96cf;
    --ink:#333;
    --muted:#8a8a8a;
    --line:#e4e4e4;
    --footer:#f5f5f5;
    --dark-btn:#555;
    --social-blue:#4a66ad;
  }
  *{box-sizing:border-box;margin:0;padding:0}
  html,body{width:880px;height:1200px;overflow:hidden;background:#fff}
  body{font-family:"Open Sans",Arial,sans-serif;color:var(--ink);position:relative}
  .abs{position:absolute}

  .topbar{left:0;top:0;width:880px;height:82px;background:var(--sky)}
  .brand{left:100px;top:22px;display:flex;align-items:center;gap:8px;color:#fff;font-size:28px;font-weight:600;letter-spacing:-.5px}
  .brand-dot{width:30px;height:30px;border-radius:50%;background:#fff}
  .login-btn{left:672px;top:27px;width:110px;height:27px;background:var(--login);color:#fff;font-size:12px;text-align:center;line-height:27px;border-radius:2px;border:1px solid #185e9e}

  .hero{left:0;top:82px;width:880px;height:359px;overflow:hidden}
  .hero-photo{position:absolute;inset:0;background:linear-gradient(100deg,#fff 0%,#fff 38%,#f1e6dc 52%,#d9b49a 66%,#7d8ca3 84%,#5d6f8b 100%)}
  .hero-copy{position:absolute;left:95px;top:92px}
  .hero-kicker{font-size:19px;color:var(--link-blue);font-weight:400}
  .hero-title{font-size:33px;color:var(--orange);font-weight:400;line-height:1.1;margin-left:-2px}
  .hero-body{font-size:10px;color:var(--muted);line-height:15px;margin-top:7px;width:320px}
  .hero-price{font-size:18px;margin-top:8px}
  .cta{display:block;margin-top:12px;width:129px;height:30px;background:linear-gradient(#fa9b27,var(--orange-deep));color:#fff;font-size:12.5px;text-align:center;line-height:30px;border-radius:2px}

  .samples-head{left:0;top:468px;width:880px;text-align:center}
  .samples-head h2{font-size:22px;font-weight:300}
  .samples-head p{font-size:9.5px;color:#666;line-height:17px;width:560px;margin:7px auto 0}

  .grid{left:92px;top:560px;width:698px;height:189px;display:grid;grid-template-columns:repeat(4,1fr);grid-template-rows:repeat(2,1fr);border:1px solid var(--line)}
  .tile{border-right:1px solid var(--line);border-bottom:1px solid var(--line);padding:16px 0 0 14px;display:flex;gap:9px}
  .tile:nth-child(4n){border-right:none}
  .tile:nth-child(n+5){border-bottom:none}
  .thumb{width:57px;height:60px;flex:none}
  .tile h3{font-size:14px;font-weight:400;color:var(--link-blue);line-height:16px}
  .tile p{font-size:8px;color:var(--muted);line-height:12px;margin-top:1px}
  .tile .more{font-size:8px;font-weight:600;color:#222;margin-top:5px;display:block}

  .points{left:94px;top:793px;width:700px;display:flex}
  .point{display:flex;gap:8px;width:245px}
  .point .pic{width:66px;height:66px;border-radius:50%;flex:none;border:1px solid #e6e6e6}
  .point h4{font-size:12.5px;font-weight:400;line-height:17px;margin-top:2px}
  .point p{font-size:8.5px;color:var(--muted);line-height:12px;margin-top:4px}

  .signup{left:0;top:906px;width:880px;height:218px;background:linear-gradient(var(--sky-band-top),var(--sky-band-bottom));text-align:center;color:#fff}
  .signup h2{font-size:22px;font-weight:400;margin-top:20px}
  .signup p{font-size:10.5px;line-height:15px;width:540px;margin:6px auto 0;color:#eaf5fc}
  .email{display:block;margin:14px auto 0;width:306px;height:27px;background:#fff;border-radius:3px;text-align:left;padding-left:11px;font-size:11px;line-height:27px;color:#aaa}
  .actions{display:flex;justify-content:center;align-items:center;gap:14px;margin-top:17px}
  .btn-dark{width:127px;height:23px;background:var(--dark-btn);border:1px solid #444;font-size:8px;font-weight:700;line-height:21px;border-radius:2px}
  .or{font-size:11px}
  .btn-social{width:128px;height:23px;background:var(--social-blue);border:1px solid #3b548f;font-size:8px;font-weight:700;border-radius:2px;display:flex;align-items:center;gap:7px;padding-left:5px}
  .btn-social i{width:14px;height:14px;background:#fff;display:block}

  .footer{left:0;top:1124px;width:880px;height:76px;background:var(--footer)}
  .footer nav{position:absolute;left:94px;top:20px;font-size:11px;color:#444;word-spacing:2px}
  .footer small{position:absolute;left:94px;top:44px;font-size:9px;color:#777}
  .social{position:absolute;left:716px;top:22px;display:flex;gap:8px}
  .social span{width:17px;height:17px;border-radius:50%;background:#666;display:block}
</style>
</head>
<body>
  <header class="abs topbar"></header>
  <div class="abs brand"><span class="brand-dot"></span>Olvantra</div>
  <div class="abs login-btn">Member Login</div>

  <section class="abs hero">
    <div class="hero-photo" role="img" aria-label="Smiling young man wearing headphones, looking at his phone"></div>
    <div class="hero-copy">
      <div class="hero-kicker">Phasellus felis dolor scelerisque</div>
      <h1 class="hero-title">Crasa ante vitae enim</h1>
      <p class="hero-body">Aliquam nec erat at purus cursus interdum Vestibulum ligula augue bibendum accumsan vestibulum ut commodo</p>
      <div class="hero-price">Only $9.99 per month</div>
      <span class="cta">Start Free Trail</span>
    </div>
  </section>

  <div class="abs samples-head">
    <h2>Sample of What Your Can Listen to on Olvantra</h2>
    <p>Suspendisse quam leo molestie sed luctus quis feugiat in pede Fusce tellus Sed metus augue convallis et vehicula ut pulvinar eu ante Integer orci tellus tristique vitae consequat nec porta vel lectus Nulla sit amet diam Duis non nunc</p>
  </div>

  <div class="abs grid">
    <div class="tile"><div class="thumb" role="img" aria-label="Audiobook cover art" style="background:linear-gradient(#3c3c3c,#111)"></div><div><h3>Audiobooks</h3><p>Aliquam nec erat at<br>purus cursus inte</p><span class="more">CLICK HERE</span></div></div>
    <div class="tile"><div class="thumb" role="img" aria-label="Stand-up comedy album art" style="background:linear-gradient(#9a8f7c,#5a5147)"></div><div><h3>Stand-up<br>Comedy</h3><p>Aliquam nec erat at</p><span class="more">CLICK HERE</span></div></div>
    <div class="tile"><div class="thumb" role="img" aria-label="Language course cover art" style="background:linear-gradient(#2a9ad8,#0d3e6a)"></div><div><h3>Language<br>Learning</h3><p>Aliquam nec erat at</p><span class="more">CLICK HERE</span></div></div>
    <div class="tile"><div class="thumb" role="img" aria-label="Memoir cover art" style="background:linear-gradient(#d9d3c4,#7fb75a)"></div><div><h3>Biographeis<br>&amp; Memories</h3><p>Aliquam nec erat at</p><span class="more">CLICK HERE</span></div></div>
    <div class="tile"><div class="thumb" role="img" aria-label="Meditation album art" style="background:linear-gradient(#b0457e,#5b3a78)"></div><div><h3>Guided<br>Meditations</h3><p>Aliquam nec erat at</p><span class="more">CLICK HERE</span></div></div>
    <div class="tile"><div class="thumb" role="img" aria-label="Business training cover art" style="background:linear-gradient(#7a3a1c,#1c1c1c)"></div><div><h3>Business<br>Training</h3><p>Aliquam nec erat at</p><span class="more">CLICK HERE</span></div></div>
    <div class="tile"><div class="thumb" role="img" aria-label="Celebrity interview cover art" style="background:linear-gradient(#8a5a3a,#c9a26a)"></div><div><h3>Celebrity<br>Interviews</h3><p>Aliquam nec erat at</p><span class="more">CLICK HERE</span></div></div>
    <div class="tile"><div class="thumb" role="img" aria-label="Fitness program cover art" style="background:linear-gradient(#3cb3e0,#1d7fb0)"></div><div><h3>Fitness<br>Programs</h3><p>Aliquam nec erat at</p><span class="more">CLICK HERE</span></div></div>
  </div>

  <div class="abs points">
    <div class="point"><div class="pic" role="img" aria-label="Phone and tablet illustration" style="background:radial-gradient(#3b6fb8,#10284f)"></div><div><h4>Listen on you Zentro,<br>Slato or Orbix Device</h4><p>Aliquam nec erat at purus cursus<br>interdum Vestibulum ligula</p></div></div>
    <div class="point"><div class="pic" role="img" aria-label="Happy couple illustration" style="background:radial-gradient(#e9c6a8,#9fc9cf)"></div><div><h4>All you can enjoy for<br>one low monthly price</h4><p>Aliquam nec erat at purus cursus<br>interdum Vestibulum</p></div></div>
    <div class="point"><div class="pic" role="img" aria-label="Red cancel button illustration" style="background:radial-gradient(#e0322c 0 30%,#fff 34%)"></div><div><h4>No Obligation.<br>Cancel any time.</h4><p>Aliquam nec erat at purus cursus<br>interdum Vestibulum ligula</p></div></div>
  </div>

  <section class="abs signup">
    <h2>Start Your Free Trail</h2>
    <p>Etiam eu urna Sed porta Suspendisse quam leo molestie sed luctus quis feugiat in pede Fusce tellus Sed metus augue convallis et vehicula ut pulvinar eu ante Integer orci tellus</p>
    <span class="email">email address</span>
    <div class="actions">
      <span class="btn-dark">Get Instant Access</span>
      <span class="or">Or</span>
      <span class="btn-social"><i></i>Sign Up Using Chatterly</span>
    </div>
  </section>

  <footer class="abs footer">
    <nav>About Us &nbsp;| &nbsp;Help &nbsp;| &nbsp;Contact Us &nbsp;| &nbsp;Member Login &nbsp;| &nbsp;Privacy Policy &nbsp;| &nbsp;Terms of Service</nav>
    <small>© 2014 Company Name &nbsp;All right reserved &nbsp;Term of Use</small>
    <div class="social" aria-label="Social links"><span></span><span></span><span></span></div>
  </footer>
</body>
</html>
```